Marcelo Quintana Postcard/Rack Card

Marcelo Quintana
Tenor & Vocal Coach
mqvoice@brivamail.com
(713) 582-6031
www.voicefromthecore.com
Want two sided postcard / rack card.4" x 9"
Front - vertical - picture in t-shirt, name, title (Tenor & Vocal Coach), contact information
Back - horizontal - picture in jacket, name, title (Tenor & Vocal Coach), contact information, bio (see attachment for words)
Do not leave space for an address.
Looking for an edgy modern design!

Target Market(s)

Young adults

Requirements
Nice to have
• Will pay extra to get a complimentary business card design, two sided

```html
<!DOCTYPE html>
<html lang="en">
<head>
<meta charset="utf-8">
<title>Marcelo Quintana – Tenor &amp; Vocal Coach</title>
<link rel="stylesheet" href="https://fonts.googleapis.com/css2?family=Great+Vibes&family=PT+Sans:wght@400;700&family=Ubuntu:wght@400&display=swap">
<style>
  :root {
    --backdrop: #414042;
    --card: #ffffff;
    --ink: #1f1f1f;
    --accent: #5b4f6c;
    --script: #b5aea6;
    --script-dark: #8f877f;
    --photo-top: #e9dca0;
    --photo-mid: #c7a98a;
    --photo-low: #2a3550;
    --notes: #e6e6e6;
  }
  * { margin: 0; padding: 0; box-sizing: border-box; }
  html, body {
    width: 1200px; height: 576px; overflow: hidden;
    background: var(--backdrop);
  }
  .rack-card {
    position: absolute; left: 51px; top: 44px;
    width: 1097px; height: 487px;
    background: var(--card);
    overflow: hidden;
  }
  .portrait {
    position: absolute; left: 0; top: 0;
    width: 258px; height: 487px;
    background: linear-gradient(170deg, var(--photo-top) 0%, var(--photo-mid) 38%, #7c7a86 55%, var(--photo-low) 80%);
  }
  .staff-decor {
    position: absolute; left: 258px; top: 0;
    width: 470px; height: 487px;
    background: radial-gradient(ellipse at 35% 75%, var(--notes) 0%, rgba(230,230,230,0.35) 45%, rgba(255,255,255,0) 75%);
  }
  .name {
    position: absolute; left: 282px; top: 30px;
    width: 310px;
    font-family: "Great Vibes", cursive;
    font-size: 78px; line-height: 66px;
    color: var(--script);
    text-shadow: 1px 2px 2px rgba(0,0,0,0.25);
  }
  .name span { display: block; }
  .name .last { padding-left: 80px; }
  .title {
    position: absolute; left: 282px; top: 183px; width: 292px;
    text-align: right;
    font-family: "PT Sans", sans-serif; font-weight: 700;
    font-size: 16px; color: var(--accent);
  }
  .bio {
    position: absolute; left: 638px; top: 47px; width: 420px;
    font-family: "PT Sans", sans-serif;
    font-size: 15.5px; line-height: 20.5px; color: var(--ink);
  }
  .bio p { margin-bottom: 12px; }
  .contact {
    position: absolute; left: 638px; top: 348px;
    font-family: "Ubuntu", sans-serif; color: var(--accent);
  }
  .contact .phone { font-size: 28px; line-height: 36px; }
  .contact .email { font-size: 18px; line-height: 24px; }
  .contact .web {
    font-family: "PT Sans", sans-serif; font-weight: 700;
    font-size: 23px; margin-top: 10px;
  }
</style>
</head>
<body>
  <main class="rack-card">
    <div class="portrait" role="img" aria-label="Portrait photo of the tenor in a dark blue jacket and white shirt"></div>
    <div class="staff-decor" role="img" aria-label="Faint decorative music staff with treble clef and notes"></div>

    <h1 class="name"><span class="first">Marcelo</span><span class="last">Quintana</span></h1>
    <p class="title">Tenor &amp; Vocal Coach</p>

    <section class="bio">
      <p>Marcelo is a local singer and actor who has been working professionally around the country as a concert artist and musical theater performer.</p>
      <p>He studied at the Whitlock School of Music, Gulf Coast University and works as a vocal coach with local youths and adults in Houston area.</p>
      <p>Marcelo’s goal is to help his students master their individual instrument so that they can achieve a natural and effortless vocal production.</p>
      <p>For more information please contact Marcelo today!</p>
    </section>

    <section class="contact">
      <p class="phone">Call Me: (713) 582-6031</p>
      <p class="email">email: mqvoice@brivamail.com</p>
      <p class="web">www.voicefromthecore.com</p>
    </section>
  </main>
</body>
</html>
```